Business Card Design for Vel
Fun, earthy, organic food company needs professional cards to speak our message!
Business Card Design for Vel -
Creative Brief
Bright & Fun-filled
Marcus Dell
Managing Member & Co-Founder
PO Box 482937 Dallas, TX 75318-2937
mdell@ourvelway.com
http:\\www.ourvelway.com
If you can access the closed project, we'll be using logo #84 in the folowing link: http://www.kavdrafthub.com/contests/logo-for-vel. We'll be uploading the logo file shortly for this project. We like simple, fun and creative but are open to many designs and styles.
The back of the card should be our logo colors, green and brown. It could be a cool design based off of the colors, you could use the entire length of the back with the logo or place both colors on the back with it being split with a similar design of the tree in our logo. We're open to your creativity!
quelldraw quelldraw
@KR - working on it now & submit our conmcepts soon! Thanks
Fovra Fovra
Please Check top right message box of the page.
trolen447 trolen447
Designers, We're looking to expedite the process on this. First come first serve on the card design. If you provide designs for stationary as well and we choose you, we'll provide a $50 donation to you. We're even open to selecting two winners for business card and stationary. So submit for each, because you could win for either or both! Thanks!

```html
<!DOCTYPE html>
<html lang="en">
<head>
<meta charset="utf-8">
<title>Vel Business Card</title>
<link rel="stylesheet" href="https://fonts.googleapis.com/css2?family=Cabin:wght@400;600;700&display=swap">
<style>
  :root {
    --backdrop: #ece7e1;
    --card-white: #ffffff;
    --leaf-green: #8cc63f;
    --earth-brown: #4a2c1a;
    --text-light: #ffffff;
  }
  html, body {
    margin: 0;
    padding: 0;
    width: 1200px;
    height: 780px;
    overflow: hidden;
    background: var(--backdrop);
    font-family: "Cabin", sans-serif;
  }
  .card {
    position: absolute;
    left: 75px;
    top: 90px;
    width: 1050px;
    height: 600px;
    border-radius: 32px;
    overflow: hidden;
    background: var(--card-white);
    box-shadow: 0 10px 30px rgba(60, 40, 20, 0.25);
  }
  .card__wave {
    position: absolute;
    inset: 0;
    width: 1050px;
    height: 600px;
  }
  .brand {
    position: absolute;
    left: 170px;
    top: 170px;
    display: flex;
    align-items: center;
    gap: 22px;
  }
  .brand__square {
    width: 70px;
    height: 70px;
    background: var(--earth-brown);
  }
  .brand__name {
    font-size: 96px;
    font-weight: 700;
    color: var(--earth-brown);
    line-height: 1;
  }
  .contact {
    position: absolute;
    right: 58px;
    top: 48px;
    text-align: right;
    color: var(--text-light);
  }
  .contact__name {
    margin: 0;
    font-size: 36px;
    font-weight: 700;
  }
  .contact__title {
    margin: 4px 0 0;
    font-size: 25px;
    line-height: 1.25;
  }
  .contact__address {
    margin: 56px 0 0;
    font-size: 23px;
    line-height: 1.3;
  }
  .contact__lines {
    list-style: none;
    margin: 26px 0 0;
    padding: 0;
    font-size: 23px;
    line-height: 1.6;
  }
  .contact__lines li {
    display: flex;
    justify-content: flex-end;
    align-items: center;
    gap: 14px;
  }
  .contact__icon {
    width: 20px;
    height: 20px;
    flex: none;
  }
</style>
</head>
<body>
  <section class="card">
    <svg class="card__wave" viewBox="0 0 1050 600" aria-hidden="true">
      <path fill="#4a2c1a" d="M0 430 C 180 380, 380 440, 470 300 C 478 288, 484 276, 490 264 C 470 330, 400 420, 200 430 C 120 434, 60 450, 0 470 Z"/>
      <path fill="#8cc63f" d="M600 0 L1050 0 L1050 600 L0 600 L0 488 C 80 462, 160 450, 240 446 C 420 438, 500 340, 540 200 C 560 120, 575 50, 600 0 Z"/>
    </svg>

    <div class="brand">
      <span class="brand__square"></span>
      <span class="brand__name">Vel</span>
    </div>

    <div class="contact">
      <p class="contact__name">Marcus Dell</p>
      <p class="contact__title">Managing Member &amp;<br>Co-Founder</p>
      <p class="contact__address">PO Box 482937<br>Dallas, TX 75318-2937</p>
      <ul class="contact__lines">
        <li>214-555-0187
          <svg class="contact__icon" viewBox="0 0 20 20"><path fill="#fff" d="M4 2 L7 2 L8.5 6 L6.5 7.5 C7.5 10 10 12.5 12.5 13.5 L14 11.5 L18 13 L18 16 C18 17 17 18 16 18 C8.5 17.5 2.5 11.5 2 4 C2 3 3 2 4 2 Z"/></svg>
        </li>
        <li>mdell@ourvelway.com
          <svg class="contact__icon" viewBox="0 0 20 20"><rect x="2" y="4" width="16" height="12" rx="1.5" fill="#fff"/><path d="M2.5 5 L10 11 L17.5 5" fill="none" stroke="#8cc63f" stroke-width="1.6"/></svg>
        </li>
        <li>www.ourvelway.com
          <svg class="contact__icon" viewBox="0 0 20 20"><circle cx="10" cy="10" r="8" fill="none" stroke="#fff" stroke-width="1.8"/><ellipse cx="10" cy="10" rx="3.5" ry="8" fill="none" stroke="#fff" stroke-width="1.4"/><line x1="2" y1="10" x2="18" y2="10" stroke="#fff" stroke-width="1.4"/></svg>
        </li>
      </ul>
    </div>
  </section>
</body>
</html>
```